Quillmark Hall Business Card

I need a business card design. We are a collaborate online training company. Our colors are gray and green. Our website is QuillmarkHall.com

I would like an area for a profile picture within the card

```html
<!DOCTYPE html>
<html lang="en">
<head>
<meta charset="utf-8">
<title>Quillmark Hall Business Card</title>
<link rel="stylesheet" href="https://fonts.googleapis.com/css2?family=Roboto+Condensed:wght@700&family=Open+Sans:wght@400&display=swap">
<style>
  :root {
    --bg: #e9e9e6;
    --green: #8cc63f;
    --green-deep: #3aa521;
    --green-light: #b3dc6c;
    --ink: #1b1b1b;
    --gray-text: #555;
    --card: #ffffff;
    --card-shade: #ececec;
  }
  * { margin: 0; padding: 0; box-sizing: border-box; }
  html, body { width: 1200px; height: 1023px; overflow: hidden; }
  body { background: var(--bg); position: relative; font-family: "Open Sans", sans-serif; }

  .card {
    position: absolute;
    width: 630px; height: 360px;
    border-radius: 18px;
    overflow: hidden;
    background: var(--card);
    box-shadow: 0 6px 18px rgba(0,0,0,.18);
  }
  .card--front { left: 60px; top: 70px; }
  .card--back  { left: 510px; top: 590px; background: linear-gradient(180deg, #fff, var(--card-shade)); }

  /* front */
  .front__glow {
    position: absolute; right: 0; top: 0; width: 280px; height: 100%;
    background: radial-gradient(ellipse at 90% 45%, var(--green-deep) 0%, #6cc23a 30%, rgba(140,198,63,.35) 60%, rgba(255,255,255,0) 82%);
  }
  .front__band-top {
    position: absolute; right: 0; top: 0; width: 300px; height: 40px;
    background: linear-gradient(90deg, rgba(140,198,63,.6), var(--green));
  }
  .front__band-bottom {
    position: absolute; left: 0; bottom: 0; width: 310px; height: 40px;
    background: linear-gradient(90deg, var(--green), rgba(140,198,63,.55));
  }
  .wordmark {
    display: flex; align-items: center; gap: 12px;
    font-family: "Roboto Condensed", sans-serif; font-weight: 700;
    color: var(--ink); letter-spacing: -0.5px; white-space: nowrap;
  }
  .wordmark__dot { border-radius: 50%; background: var(--green); flex: none; }
  .front__wordmark { position: absolute; left: 60px; top: 62px; font-size: 40px; }
  .front__wordmark .wordmark__dot { width: 34px; height: 34px; }

  .profile {
    position: absolute; left: 44px; top: 162px;
    width: 130px; height: 130px; border-radius: 50%;
    border: 2px solid var(--green);
    background: linear-gradient(135deg, #f0d2b2 0%, #c9a27a 50%, #4a4a4a 100%);
  }
  .person { position: absolute; left: 196px; top: 168px; }
  .person__name { font-size: 17px; color: var(--gray-text); margin-bottom: 22px; }
  .contacts { list-style: none; }
  .contacts li { display: flex; align-items: center; gap: 10px; font-size: 13px; color: #333; margin-bottom: 7px; white-space: nowrap; }
  .contacts svg { width: 16px; height: 16px; flex: none; }

  /* back */
  .back__band {
    position: absolute; left: 0; width: 100%; height: 92px;
  }
  .back__band--top { top: 0; }
  .back__band--bottom { bottom: 0; }
  .back__wordmark {
    position: absolute; left: 50%; top: 50%; transform: translate(-50%, -50%);
    font-size: 54px;
  }
  .back__wordmark .wordmark__dot { width: 46px; height: 46px; }
</style>
</head>
<body>

<section class="card card--front" aria-label="Business card front">
  <div class="front__glow"></div>
  <div class="front__band-top"></div>
  <div class="front__band-bottom"></div>

  <div class="wordmark front__wordmark">
    <span class="wordmark__dot"></span>
    <span class="wordmark__name">Quillmark Hall</span>
  </div>

  <div class="profile" role="img" aria-label="Profile photo of the card holder"></div>

  <div class="person">
    <p class="person__name">Your name</p>
    <ul class="contacts">
      <li>
        <svg viewBox="0 0 16 16" aria-hidden="true"><circle cx="8" cy="8" r="7" fill="none" stroke="#8cc63f" stroke-width="1.3"/><path d="M5.5 4.8l1.3-.3.8 1.8-.8.6c.4.9 1 1.5 1.9 1.9l.6-.8 1.8.8-.3 1.3c-3 .2-5.5-2.3-5.3-5.3z" fill="#8cc63f"/></svg>
        44-555-01927
      </li>
      <li>
        <svg viewBox="0 0 16 16" aria-hidden="true"><rect x="1.5" y="3.5" width="13" height="9" fill="none" stroke="#8cc63f" stroke-width="1.3"/><path d="M1.5 3.5l6.5 5 6.5-5" fill="none" stroke="#8cc63f" stroke-width="1.3"/></svg>
        info@quillmarkhall.com
      </li>
      <li>
        <svg viewBox="0 0 16 16" aria-hidden="true"><g fill="none" stroke="#8cc63f" stroke-width="1.2"><circle cx="8" cy="8" r="6.5"/><ellipse cx="8" cy="8" rx="3" ry="6.5"/><path d="M1.5 8h13M2.5 5h11M2.5 11h11"/></g></svg>
        www.quillmarkhall.com
      </li>
    </ul>
  </div>
</section>

<section class="card card--back" aria-label="Business card back">
  <svg class="back__band back__band--top" viewBox="0 0 630 92" preserveAspectRatio="none" aria-hidden="true">
    <polygon points="0,0 630,0 630,40 560,78 0,78" fill="#8cc63f"/>
    <polygon points="0,78 560,78 556,86 0,86" fill="#1b1b1b"/>
  </svg>
  <svg class="back__band back__band--bottom" viewBox="0 0 630 92" preserveAspectRatio="none" aria-hidden="true">
    <polygon points="70,6 630,6 630,14 66,14" fill="#1b1b1b"/>
    <polygon points="66,14 630,14 630,92 0,92 0,52" fill="#8cc63f"/>
  </svg>
  <div class="wordmark back__wordmark">
    <span class="wordmark__dot"></span>
    <span class="wordmark__name">Quillmark Hall</span>
  </div>
</section>

</body>
</html>
```